The Lindenmoor Compass Book

Cover Design for my first book. The book is for elementary school principals who are unhappy and are considering a career change but are afraid to leave. I teach them how to develop emotional fitness and resiliency through thought management so that they can decide whether to stay or leave their position from a place of empowerment. I've attached my podcast artwork for your reference. My publisher suggested not having me on the cover which is fine. I just thought it might be helpful.

Target Market(s)

Elementary School Principals

Industry/Entity Type

Education

Logo Text

The Lindenmoor Compass

Font styles to use
Serif
Sans Serif

Colors
34a6d7
33b8a4
3276b5

Requirements
Must have
• Title, Author name, photo or artwork that captures the essence of the book

```html
<!DOCTYPE html>
<html lang="en">
<head>
<meta charset="utf-8">
<title>The Lindenmoor Compass — Book Cover</title>
<link href="https://fonts.googleapis.com/css2?family=Raleway:wght@200;300;700;800&display=swap" rel="stylesheet">
<style>
  :root {
    --stage-bg: #e9ecef;
    --cover-blue: #3276b5;
    --ink-dark: #1d2530;
    --ink-light: #ffffff;
    --cover-shadow: rgba(10, 25, 45, 0.35);
  }
  * { margin: 0; padding: 0; box-sizing: border-box; }
  html, body {
    width: 1200px;
    height: 1000px;
    overflow: hidden;
    background: var(--stage-bg);
  }
  .stage {
    position: relative;
    width: 1200px;
    height: 1000px;
  }
  .book-cover {
    position: absolute;
    left: 362px;
    top: 138px;
    width: 476px;
    height: 724px;
    background: var(--cover-blue);
    box-shadow: 0 8px 24px var(--cover-shadow);
    font-family: "Raleway", "Helvetica Neue", Arial, sans-serif;
  }
  .title {
    position: absolute;
    left: 101px;
    top: 96px;
    line-height: 1;
  }
  .title-lead {
    display: block;
    font-weight: 300;
    font-size: 26px;
    color: var(--ink-dark);
    letter-spacing: 0.5px;
  }
  .title-main {
    display: block;
    margin-top: 18px;
    font-weight: 800;
    font-size: 46px;
    line-height: 62px;
    color: var(--ink-light);
    letter-spacing: 0.5px;
  }
  .title-tail {
    display: block;
    margin-top: 6px;
    font-weight: 200;
    font-size: 48px;
    color: var(--ink-dark);
    letter-spacing: 0.5px;
  }
  .cover-artwork {
    position: absolute;
    left: 123px;
    top: 405px;
    width: 235px;
    height: 145px;
  }
  .author {
    position: absolute;
    left: 0;
    right: 0;
    top: 682px;
    text-align: center;
    font-weight: 700;
    font-size: 14px;
    letter-spacing: 0.8px;
    color: var(--ink-dark);
  }
</style>
</head>
<body>
  <main class="stage">
    <section class="book-cover">
      <h1 class="title">
        <span class="title-lead">THE</span>
        <span class="title-main">LINDEN-<br>MOOR</span>
        <span class="title-tail">COMPASS</span>
      </h1>
      <svg class="cover-artwork" viewBox="0 0 235 145" role="img" aria-label="White silhouette of two flexed arms showing strength">
        <rect x="0" y="0" width="235" height="145" rx="14" fill="#ffffff" fill-opacity="0.9"/>
      </svg>
      <p class="author">MARISA JOAN HOLLOWAY</p>
    </section>
  </main>
</body>
</html>
```